you will use Ai to Copy the website Quellabyx.com to come up with the basic frame work and it will give you the understanding of how I would like Zandoprik.com to be like. Zandoprik.com is a peer to peer rv rental site very similar to both of the other rv rental sites the difference is that are commission based 20% and above per rental and we will be one flat monthly rate and they keep all the earnings. Below is photo that will help you with the color scheme and the look and feel of the design

```html
<!DOCTYPE html>
<html lang="en">
<head>
<meta charset="utf-8">
<title>Zandoprik.com – The RV Marketplace That Puts Owners First</title>
<link href="https://fonts.googleapis.com/css2?family=Oswald:wght@500;600&family=Poppins:wght@400;500;600&display=swap" rel="stylesheet">
<style>
:root{
  --bg:#020b1c;
  --panel:#0a1b40;
  --panel-deep:#071530;
  --line:#1f3d80;
  --green:#9ccb3b;
  --green-dark:#5f9a1d;
  --white:#ffffff;
  --soft:#d9e0ee;
  --muted:#8d9ab5;
  --red:#ff3b3b;
  --blue-link:#3a7bff;
}
*{box-sizing:border-box;margin:0;padding:0}
html,body{width:1200px;height:2479px;overflow:hidden}
body{background:var(--bg);color:var(--white);font-family:'Poppins',sans-serif;position:relative}
.abs{position:absolute}
.display{font-family:'Oswald',sans-serif;font-weight:600;text-transform:uppercase;letter-spacing:1px}
.green{color:var(--green)}
.btn{position:absolute;display:flex;align-items:center;justify-content:center;background:linear-gradient(180deg,#a3d13f,var(--green-dark));color:#0b1a05;font-size:10px;font-weight:500;border-radius:3px;box-shadow:0 2px 6px rgba(0,0,0,.4)}

/* hero */
.hero-photo{left:430px;top:0;width:770px;height:520px;
  background:
   radial-gradient(circle at 58% 30%,rgba(255,170,40,.95) 0,rgba(240,120,20,.55) 10%,rgba(90,50,20,.35) 28%,transparent 48%),
   radial-gradient(ellipse at 70% 75%,rgba(40,50,30,.9),transparent 60%),
   linear-gradient(180deg,#1a1c24 0%,#3b3228 40%,#1d2418 75%,var(--bg) 100%);
  -webkit-mask-image:linear-gradient(90deg,transparent 0,#000 35%);mask-image:linear-gradient(90deg,transparent 0,#000 35%)}
.nav{left:0;top:0;width:1200px;height:74px}
.logo{position:absolute;font-weight:600;font-size:24px;color:var(--white);display:flex;align-items:center;gap:6px}
.logo .dot{width:9px;height:9px;background:var(--green);border-radius:50%}
.nav-links{position:absolute;left:441px;top:30px;display:flex;gap:22px;font-size:10px}
.login{left:946px;top:30px;font-size:10px}
.tag{left:144px;top:137px;width:189px;height:28px;background:#0d2150;color:var(--green);font-size:12px;display:flex;align-items:center;justify-content:center;letter-spacing:.5px}
.hero-title{left:144px;top:176px;font-size:48px;line-height:51px}
.hero-sub{left:145px;top:341px;font-size:12px;line-height:20px}

/* search */
.search{left:143px;top:504px;width:914px;height:102px;background:var(--panel-deep);border:1.5px solid var(--line);border-radius:10px}
.field{position:absolute;top:30px;font-size:10.5px}
.field .label{color:var(--green);font-weight:500;letter-spacing:.5px;display:flex;align-items:center;gap:6px;margin-left:-22px}
.field .value{margin-top:5px}
.sep{position:absolute;top:20px;width:1.5px;height:62px;background:var(--line)}

/* categories */
.center{left:0;width:1200px;text-align:center}
.sec-title{font-size:20px;letter-spacing:.5px}
.card{position:absolute;top:762px;width:217px;height:256px;border:1.5px solid var(--line);border-radius:12px;overflow:hidden;background:var(--panel-deep)}
.card .ph{height:185px;background:linear-gradient(180deg,#7c8f99,#3c4a52 70%,var(--panel-deep))}
.card .cat{position:absolute;left:23px;top:203px;color:var(--green);font-size:11px;font-weight:500;letter-spacing:.8px}
.card .desc{position:absolute;left:23px;top:222px;font-size:10px}

/* compare */
.eyebrow{left:143px;top:1149px;font-size:12px;color:var(--green);letter-spacing:.5px}
.big-title{left:142px;top:1178px;font-size:48px;line-height:51px}
.body-copy{left:143px;top:1342px;width:280px;font-size:12px;line-height:20px;letter-spacing:.3px}
.cmp{position:absolute;top:1154px;width:284px;height:272px;background:var(--panel-deep);border:1.5px solid var(--line);border-radius:8px}
.cmp.win{border-color:var(--green)}
.cmp h3{text-align:center;margin-top:24px;font-size:16px}
.cmp .sub{text-align:center;font-size:11px;margin-top:6px;letter-spacing:.5px}
.row{position:absolute;left:21px;width:236px;font-size:11.5px;display:flex;justify-content:space-between;padding:0 8px}
.rule{position:absolute;left:21px;width:236px;height:1px;background:#23407a}
.cmp .note{position:absolute;left:0;width:100%;text-align:center;top:240px;font-size:9px}
.glow{position:absolute;bottom:-2px;left:60px;width:164px;height:3px;border-radius:2px}
.vs{left:739px;top:1268px;width:46px;height:46px;border-radius:50%;background:#fff;color:#0a1430;display:flex;align-items:center;justify-content:center;font-family:'Oswald',sans-serif;font-weight:600;font-size:16px}

/* pricing */
.plan{left:144px;top:1556px;width:444px;height:284px;background:var(--panel-deep);border:1.5px solid var(--line);border-radius:8px}
.feat{position:absolute;font-size:12px;display:flex;flex-direction:column;gap:6px;letter-spacing:.3px}
.feat span{display:flex;align-items:center;gap:6px}
.promo{left:612px;top:1556px;width:444px;height:284px;border-radius:8px;overflow:hidden;
  background:linear-gradient(160deg,#6d7479 0%,#3e4a45 45%,#27321f 75%,#1b1f1c 100%)}
.promo-shade{position:absolute;inset:0;background:linear-gradient(90deg,rgba(10,15,20,.55),transparent 70%)}

/* testimonials */
.tcard{position:absolute;top:1965px;width:298px;height:184px;background:var(--panel-deep);border:1.5px solid var(--line);border-radius:8px}
.avatar{position:absolute;left:20px;top:18px;width:44px;height:44px;border-radius:50%;background:linear-gradient(160deg,#b8c4d6,#55677f)}
.tname{position:absolute;left:74px;top:22px;font-size:12px;font-weight:500}
.trole{position:absolute;left:74px;top:42px;font-size:9.5px;color:var(--blue-link)}
.tquote{position:absolute;left:74px;top:66px;width:200px;font-size:10.5px;line-height:16.5px}
.qmark{position:absolute;right:18px;bottom:-44px;font-family:'Oswald',sans-serif;font-size:110px;color:#13306e;line-height:1}

/* footer */
.fhead{position:absolute;top:2231px;font-size:11px;font-weight:500}
.fhead::after{content:"";display:block;width:28px;height:2px;background:var(--green);margin-top:11px}
.flinks{position:absolute;top:2276px;font-size:10.5px;color:var(--soft);display:flex;flex-direction:column;gap:9.5px}
.footer-copy{left:144px;top:2301px;width:240px;font-size:10.5px;line-height:20px;color:var(--soft)}
.divider{left:138px;top:2433px;width:924px;height:1px;background:#1a2a4a}
</style>
</head>
<body>

<div class="abs hero-photo" role="img" aria-label="Motorhome driving on a winding mountain road through a pine forest at sunset"></div>

<header class="abs nav">
  <div class="logo" style="left:145px;top:20px"><span>Zandoprik.com</span><span class="dot"></span></div>
  <nav class="nav-links"><span>About</span><span>List yout RV</span><span>How it works</span><span>Pricing</span><span>Resources</span></nav>
  <span class="abs login">Log In</span>
  <span class="btn" style="left:992px;top:23px;width:63px;height:28px">Sign Up</span>
</header>

<div class="abs tag">LIST IT. RENT IT. BANK IT.</div>
<h1 class="abs display hero-title">The RV marketplace<br>that puts owners<br><span class="green">first.</span></h1>
<p class="abs hero-sub">List your RV for one flat monthly fee and<br><span class="green">keep 100%</span> of what you earn.</p>
<span class="btn" style="left:145px;top:397px;width:76px;height:27px">Book Now</span>

<section class="abs search">
  <div class="field" style="left:70px">
    <div class="label"><svg width="16" height="16" viewBox="0 0 24 24" fill="none" stroke="#9ccb3b" stroke-width="1.8"><path d="M12 22s7-7 7-12a7 7 0 0 0-14 0c0 5 7 12 7 12z"/><circle cx="12" cy="10" r="2.5"/></svg>WHERE TO?</div>
    <div class="value">Search city, state or campground</div>
  </div>
  <div class="sep" style="left:290px"></div>
  <div class="field" style="left:360px">
    <div class="label"><svg width="18" height="16" viewBox="0 0 24 24" fill="none" stroke="#9ccb3b" stroke-width="1.8"><rect x="3" y="5" width="18" height="16" rx="2"/><path d="M3 10h18M8 3v4M16 3v4M7 14h2M11 14h2M15 14h2M7 17h2M11 17h2"/></svg>CHECK IN</div>
    <div class="value">Add dates</div>
  </div>
  <div class="sep" style="left:454px"></div>
  <div class="field" style="left:521px">
    <div class="label"><svg width="16" height="16" viewBox="0 0 24 24" fill="none" stroke="#9ccb3b" stroke-width="1.8"><path d="M12 3l8 3v6c0 5-4 8-8 9-4-1-8-4-8-9V6z"/><path d="M8.5 12l2.5 2.5 4.5-5"/></svg>CHECK OUT</div>
    <div class="value">Add dates</div>
  </div>
  <div class="sep" style="left:628px"></div>
  <div class="field" style="left:691px">
    <div class="label"><svg width="16" height="16" viewBox="0 0 24 24" fill="none" stroke="#9ccb3b" stroke-width="1.8"><circle cx="12" cy="8" r="4"/><path d="M4 21c1-4 4-6 8-6s7 2 8 6"/></svg>GUESTS</div>
    <div class="value">2 Adults</div>
  </div>
  <span class="btn" style="left:773px;top:38px;width:90px;height:27px">SEARCH RVS</span>
</section>

<h2 class="abs center display sec-title" style="top:680px">Browse RVs by category</h2>
<p class="abs center" style="top:718px;font-size:12px">Find the perfect RV for your next adventure.</p>

<article class="card" style="left:144px"><div class="ph" role="img" aria-label="Class A motorcoach parked in the hills"></div><div class="cat">CLASS A</div><div class="desc">Luxury on the road</div></article>
<article class="card" style="left:376px"><div class="ph" role="img" aria-label="Family relaxing inside a Class C motorhome" style="background:linear-gradient(180deg,#c9b59a,#7a6a58 70%,#071530)"></div><div class="cat">CLASS C</div><div class="desc">Family friendly comfort</div></article>
<article class="card" style="left:608px"><div class="ph" role="img" aria-label="Travel trailer parked on a grassy hillside" style="background:linear-gradient(180deg,#c4cdd1,#75815f 70%,#071530)"></div><div class="cat">TRAVEL TRAILERS</div><div class="desc">Tow your adventure</div></article>
<article class="card" style="left:840px"><div class="ph" role="img" aria-label="Blue and white camper van under green trees" style="background:linear-gradient(180deg,#4f6b45,#4b6a8e 65%,#071530)"></div><div class="cat">CAMPER VANS</div><div class="desc">Go anywhere</div></article>

<span class="btn" style="left:559px;top:1045px;width:82px;height:26px">VIEW ALL</span>

<p class="abs eyebrow">WHY CHOOSE ZANDOPRIK.COM?</p>
<h2 class="abs display big-title">Keep more of<br>what you<br><span class="green">earn.</span></h2>
<p class="abs body-copy">Unlike other platforms that take a percent-age of every booking, we charge a simple one-time fee so you keep more of your hard-earned income.</p>

<div class="cmp" style="left:472px">
  <h3 class="display">Other Platforms</h3>
  <p class="sub">EX. COMPETITOR (TYPICAL)</p>
  <div class="row" style="top:98px"><span>Booking Amount</span><span>$1,000</span></div>
  <div class="rule" style="top:124px"></div>
  <div class="row" style="top:148px"><span>Platform Fee(20%)</span><span style="color:var(--red)">$200</span></div>
  <div class="rule" style="top:174px"></div>
  <div class="row" style="top:194px"><span>Owner Receives</span><span style="color:var(--red)">$800</span></div>
  <div class="rule" style="top:220px"></div>
  <p class="note" style="color:var(--red)">You lose $200 on a single booking</p>
  <div class="glow" style="background:radial-gradient(ellipse,#4a7bff,transparent 70%)"></div>
</div>
<div class="abs vs">VS</div>
<div class="cmp win" style="left:771px">
  <h3 class="display green">Zandoprik.com</h3>
  <p class="sub">ONE-TIME FEE ONLY</p>
  <div class="row" style="top:98px"><span>Booking Amount</span><span>$1,000</span></div>
  <div class="rule" style="top:124px"></div>
  <div class="row" style="top:148px"><span>Platform Fee</span><span class="green">$0</span></div>
  <div class="rule" style="top:174px"></div>
  <div class="row" style="top:194px"><span>Owner Receives</span><span class="green">$1,000</span></div>
  <div class="rule" style="top:220px"></div>
  <p class="note green">Keep $200 of your earnings!</p>
  <div class="glow" style="background:radial-gradient(ellipse,#7fe03a,transparent 70%)"></div>
</div>

<h2 class="abs center display sec-title" style="top:1501px">Simple pricing. Zero commission.</h2>

<section class="abs plan">
  <p class="abs" style="left:0;width:444px;text-align:center;top:24px;font-size:11.5px;font-weight:500">OWNER PLAN</p>
  <p class="abs" style="left:164px;top:36px;font-size:32px;font-weight:600;color:var(--green)">$39 <span style="font-size:11px;color:#fff;font-weight:400">/ Month</span></p>
  <p class="abs" style="left:0;width:444px;text-align:center;top:80px;font-size:11px">Everything you need to rent your RV</p>
  <div class="feat" style="left:56px;top:112px">
    <span><svg width="12" height="12" viewBox="0 0 12 12"><path d="M1.5 6.5l3 3 6-7" fill="none" stroke="#9ccb3b" stroke-width="1.6"/></svg>Unlimited RV Listings</span>
    <span><svg width="12" height="12" viewBox="0 0 12 12"><path d="M1.5 6.5l3 3 6-7" fill="none" stroke="#9ccb3b" stroke-width="1.6"/></svg>Unlimited Bookings</span>
    <span><svg width="12" height="12" viewBox="0 0 12 12"><path d="M1.5 6.5l3 3 6-7" fill="none" stroke="#9ccb3b" stroke-width="1.6"/></svg>Direct Messaging</span>
    <span><svg width="12" height="12" viewBox="0 0 12 12"><path d="M1.5 6.5l3 3 6-7" fill="none" stroke="#9ccb3b" stroke-width="1.6"/></svg>Calendar Management</span>
  </div>
  <div class="feat" style="left:257px;top:112px">
    <span><svg width="12" height="12" viewBox="0 0 12 12"><path d="M1.5 6.5l3 3 6-7" fill="none" stroke="#9ccb3b" stroke-width="1.6"/></svg>Secure Payments</span>
    <span><svg width="12" height="12" viewBox="0 0 12 12"><path d="M1.5 6.5l3 3 6-7" fill="none" stroke="#9ccb3b" stroke-width="1.6"/></svg>Reviews &amp; Ratings</span>
    <span><svg width="12" height="12" viewBox="0 0 12 12"><path d="M1.5 6.5l3 3 6-7" fill="none" stroke="#9ccb3b" stroke-width="1.6"/></svg>Owner Dashboard</span>
    <span><svg width="12" height="12" viewBox="0 0 12 12"><path d="M1.5 6.5l3 3 6-7" fill="none" stroke="#9ccb3b" stroke-width="1.6"/></svg>Priority Support</span>
  </div>
  <span class="btn" style="left:153px;top:216px;width:126px;height:27px">START FREE TRIAL</span>
  <p class="abs green" style="left:0;width:444px;text-align:center;top:253px;font-size:9px">Cancel anytime. No hidden fees.</p>
</section>

<section class="abs promo" role="img" aria-label="Misty mountain road winding through autumn forest">
  <div class="promo-shade"></div>
  <h3 class="abs display" style="left:25px;top:62px;font-size:19px;line-height:25px">List today.<br>Earn more.<br>Live your adventure.</h3>
  <p class="abs" style="left:25px;top:144px;width:230px;font-size:10.5px;line-height:16.5px">Join thousands of RV owners who are earning more with Zandoprik.com</p>
  <span class="btn" style="left:26px;top:194px;width:126px;height:26px">LIST YOUR RV NOW</span>
</section>

<h2 class="abs center display sec-title" style="top:1916px">Simple pricing. Zero commission.</h2>

<article class="tcard" style="left:142px">
  <div class="avatar" role="img" aria-label="Portrait of James R."></div>
  <p class="tname">James R.</p><p class="trole">Owner</p>
  <p class="tquote">Brelvane has transformed the way we manage security. Their team is responsive, knowledge-able, and truly invested in our success.</p>
  <span class="qmark">”</span>
</article>
<article class="tcard" style="left:451px">
  <div class="avatar" role="img" aria-label="Portrait of David C."></div>
  <p class="tname">David C.</p><p class="trole">Owner</p>
  <p class="tquote">From day one, Brelvane has been a trusted partner. Their proactive approach and expert support give us complete peace of mind.</p>
  <span class="qmark">”</span>
</article>
<article class="tcard" style="left:760px">
  <div class="avatar" role="img" aria-label="Portrait of Maria T." style="left:12px"></div>
  <div class="avatar" role="img" aria-label="Portrait of John T." style="left:44px"></div>
  <p class="tname" style="left:92px">Maria &amp; John T.</p><p class="trole" style="left:92px">Owner</p>
  <p class="tquote" style="left:92px;width:190px">Reliable, professional, and always one step ahead. Brelvane is an extension of our team, ensuring our business stays secure.</p>
  <span class="qmark">”</span>
</article>

<footer>
  <div class="logo" style="left:144px;top:2236px"><span>Zandoprik.com</span><span class="dot"></span></div>
  <p class="abs footer-copy">List, travel, Earn.<br>The peer-to-peer RV rental marketplace that helps you rent your RV, motorhome, campervan and more. 100% of rentals. 100% of the time.</p>
  <p class="fhead" style="left:479px">MARKETPLACE</p>
  <div class="flinks" style="left:479px"><span>Browse RVs</span><span>List Your RV</span><span>How It Works</span><span>Earn $ / Payouts</span><span>Pricing</span></div>
  <p class="fhead" style="left:621px">COMPANY</p>
  <div class="flinks" style="left:621px"><span>About Us</span><span>Careers</span><span>Blog</span><span>Contact</span></div>
  <p class="fhead" style="left:728px">SUPPORT</p>
  <div class="flinks" style="left:728px"><span>Help Center</span><span>Safety</span><span>Terms of Service</span><span>Privacy Policy</span></div>
  <p class="fhead" style="left:857px">NEWSLETTER</p>
  <p class="abs" style="left:856px;top:2276px;font-size:10.5px;color:var(--soft)">Get the vacation and road trip ideas.</p>
  <div class="abs" style="left:856px;top:2306px;width:200px;height:29px;border:1px solid #23407a;border-radius:3px;background:var(--panel-deep);font-size:8px;color:var(--muted);padding:9px 10px">Enter your email</div>
  <span class="btn" style="left:971px;top:2306px;width:86px;height:29px;font-size:10.5px">SUBSCRIBE</span>
  <div class="abs divider"></div>
  <p class="abs center" style="top:2451px;font-size:8px;color:#2c5bc8">© 2024 Zandoprik.com. All rights reserved.</p>
</footer>

</body>
</html>
```